I need a business card.

I need a simple, minimalist, business card. I think the coolest business card I have ever seen is Marty Vexler's from Brimstone Heist... it is just a little creepy for the real world.
I am a photographer and I need a card that I can give to brides or potential portrait customers that is simple and classy.
My name is Gil Anstrade. My website is www.gilanstrade-example.com
Please design my card.
I think it could be as simple as my name, phone # and website... where the rest of my contact could be found... or maybe my email and no website... I am open to ideas. I imagined the card on thick card stock with a black background...

```html
<!DOCTYPE html>
<html lang="en">
<head>
<meta charset="utf-8">
<title>Gil Anstrade — Business Card</title>
<link rel="stylesheet" href="https://fonts.googleapis.com/css2?family=Arimo:wght@700&display=swap">
<style>
  :root {
    --ink: #000000;
    --paper: #ffffff;
    --corner-tone: #17141c;
  }
  html, body {
    margin: 0;
    padding: 0;
    width: 1200px;
    height: 685px;
    overflow: hidden;
    background: var(--paper);
  }
  .card {
    position: relative;
    width: 1200px;
    height: 685px;
    background: var(--paper);
    font-family: "Arimo", Arial, sans-serif;
    font-weight: 700;
    color: var(--ink);
  }
  .card-frame {
    position: absolute;
    inset: 0;
  }
  .underlined {
    position: absolute;
    margin: 0;
    white-space: nowrap;
    line-height: 1;
  }
  .underlined::after {
    content: "";
    position: absolute;
    left: 0;
    right: 0;
    background: var(--ink);
  }
  .email {
    top: 74px;
    left: 588px;
    width: 464px;
    text-align: center;
    font-size: 34px;
  }
  .email::after { bottom: -6px; height: 4px; }
  .name {
    top: 266px;
    left: 138px;
    width: 900px;
    text-align: center;
    font-size: 124px;
    letter-spacing: 1px;
  }
  .name::after { bottom: 2px; height: 6px; }
  .website {
    top: 560px;
    left: 414px;
    width: 672px;
    text-align: center;
    font-size: 42px;
  }
  .website::after { bottom: -12px; height: 5px; }
  .social {
    position: absolute;
    left: 112px;
    top: 524px;
    font-size: 24px;
    line-height: 1;
  }
  .social-handle {
    display: block;
    margin-bottom: 14px;
  }
  .social-list {
    list-style: none;
    margin: 0;
    padding: 0;
  }
  .social-list li {
    display: flex;
    align-items: center;
    gap: 8px;
    font-size: 20px;
    line-height: 1;
    margin-bottom: 10px;
  }
  .social-list .mark {
    width: 16px;
    height: 16px;
    background: var(--ink);
  }
</style>
</head>
<body>
<div class="card">
  <svg class="card-frame" width="1200" height="685" viewBox="0 0 1200 685" xmlns="http://www.w3.org/2000/svg">
    <path fill="var(--ink)" d="M40 30 C200 18 420 34 620 22 C820 12 1000 30 1150 24 C1185 40 1172 120 1180 240 C1188 380 1168 500 1178 640 C1170 676 1120 668 1000 672 C820 680 620 664 420 676 C260 684 110 668 40 672 C14 660 24 560 18 420 C12 280 30 160 20 60 C22 38 30 32 40 30 Z"/>
    <path fill="var(--paper)" d="M90 56 C260 48 460 62 640 52 C820 44 1000 58 1128 52 C1146 70 1138 160 1144 280 C1150 400 1134 520 1142 608 C1120 632 1020 622 880 628 C700 636 520 620 340 632 C220 640 130 626 92 630 C70 600 80 500 72 380 C66 260 84 150 74 72 C76 60 82 58 90 56 Z"/>
    <rect role="img" aria-label="Four-leaf clover illustration" x="80" y="42" width="204" height="216" rx="40" fill="var(--corner-tone)"/>
  </svg>

  <p class="underlined email">gil@gilanstrade-example.com</p>
  <h1 class="underlined name">Gil Anstrade</h1>
  <p class="underlined website">www.gilanstrade-example.com</p>

  <div class="social">
    <span class="social-handle">gilthesteady</span>
    <ul class="social-list">
      <li><span class="mark"></span>Quillcast</li>
      <li><span class="mark"></span>Pagefold</li>
    </ul>
  </div>
</div>
</body>
</html>
```